New professional looking flyer for company

I need our flyer updated my flyer is the Ruv flyer Have attached current flyer so you know what services need to be listed. Want it to be in mainly dark colours like black and dark grey with pops of light grey, silver or white. i have added several photos for you to choose which ones work best with your design would like The photos to be in colour for the flyer. But can have a mix of greyscale if that works for your design j have attached another companies flyers as design ideas to show what I am looking for

Target Market(s)

new clients

Industry/Entity Type

transport and earthmoving

Colors

Designer to choose colors to be used in the design.

Requirements
Nice to have
• Look professional
Should not have
• No orange or red or green

```html
<!DOCTYPE html>
<html lang="en">
<head>
<meta charset="utf-8">
<title>Ruv Pty Ltd – Our Services Flyer</title>
<link rel="stylesheet" href="https://fonts.googleapis.com/css2?family=Barlow:wght@400;500;600;700&family=Barlow+Condensed:wght@600;700;800&display=swap">
<style>
  :root {
    --page-bg: #d9d9d9;
    --flyer-black: #0d0d0d;
    --metal-dark: #1c1c1c;
    --metal-mid: #3a3a3a;
    --gold: #dca11a;
    --white: #ffffff;
    --silver-light: #f2f2f2;
    --silver-mid: #c4c4c4;
    --ink: #111111;
  }
  * { box-sizing: border-box; margin: 0; padding: 0; }
  html, body { width: 1090px; height: 1200px; overflow: hidden; }
  body {
    background: var(--page-bg);
    font-family: "Barlow", Arial, sans-serif;
    position: relative;
  }
  .flyer {
    position: absolute;
    left: 135px; top: 20px;
    width: 820px; height: 1160px;
    background: var(--flyer-black);
    overflow: hidden;
    box-shadow: 0 6px 24px rgba(0,0,0,.35);
  }
  .header-texture {
    position: absolute; inset: 0 0 auto 0; height: 470px;
    background: radial-gradient(ellipse at 50% 30%, var(--metal-mid) 0%, var(--metal-dark) 55%, #050505 100%);
  }
  .brand {
    position: absolute; top: 150px; left: 0; right: 0;
    text-align: center; color: var(--silver-light);
  }
  .brand-name { font-weight: 700; font-size: 110px; line-height: 1; letter-spacing: 4px; }
  .brand-suffix { font-weight: 700; font-size: 22px; margin-top: 4px; }
  .photo { position: absolute; }
  .photo-roadtrain {
    left: 0; top: 300px; width: 820px; height: 170px;
    background: linear-gradient(180deg, rgba(40,40,40,0) 0%, #2c2c2c 35%, #555 70%, #3a3a3a 100%);
  }
  .photo-sunset-truck {
    left: 0; top: 480px; width: 410px; height: 290px;
    background: linear-gradient(160deg, #8aa3c0 0%, #d8c59a 40%, #b8c2cc 60%, #7a5040 100%);
    clip-path: polygon(0 4%, 90% 0, 100% 100%, 0 100%);
  }
  .services-band {
    position: absolute; left: 370px; top: 420px; width: 450px; height: 74px;
    background: var(--gold);
    clip-path: polygon(0 100%, 0 20%, 100% 0, 100% 100%);
  }
  .services-title {
    position: absolute; left: 388px; top: 424px;
    font-family: "Barlow Condensed", "Arial Narrow", sans-serif;
    font-weight: 800; font-size: 66px; line-height: 1; color: var(--ink);
    letter-spacing: 1px;
  }
  .service-list {
    position: absolute; left: 425px; top: 510px; width: 380px;
    list-style: none; color: var(--white);
    font-weight: 600; font-size: 18px; line-height: 27.5px;
  }
  .service-list li { position: relative; padding-left: 26px; }
  .service-list li::before {
    content: ""; position: absolute; left: 0; top: 7px;
    width: 15px; height: 15px; border-radius: 50%; background: var(--gold);
  }
  .service-list li::after {
    content: ""; position: absolute; left: 5px; top: 9px;
    width: 4px; height: 8px;
    border: solid var(--ink); border-width: 0 2px 2px 0;
    transform: rotate(45deg);
  }
  .service-list .multi { line-height: 20px; padding-top: 4px; padding-bottom: 4px; }
  .service-list .multi::before { top: 6px; }
  .service-list .multi::after { top: 8px; }
  .quote-callout {
    position: absolute; left: 40px; top: 790px; width: 370px;
  }
  .quote-intro { color: var(--white); font-size: 15px; font-weight: 500; white-space: nowrap; }
  .quote-headline {
    font-family: "Barlow Condensed", "Arial Narrow", sans-serif;
    font-weight: 800; font-size: 33px; line-height: 0.95;
    color: var(--gold); margin-top: 4px; text-transform: uppercase;
  }
  .photo-oversize-truck {
    left: 40px; top: 930px; width: 420px; height: 220px;
    background: linear-gradient(180deg, #d9dde0 0%, #a8adb2 45%, #6a6e72 75%, #2a2a2a 100%);
    clip-path: polygon(18% 0, 100% 12%, 100% 100%, 0 100%, 0 30%);
  }
  .contact-strip {
    position: absolute; left: 475px; width: 345px; height: 38px;
    background: linear-gradient(90deg, var(--silver-light) 0%, var(--white) 45%, var(--silver-mid) 100%);
    display: flex; align-items: center; gap: 8px; padding-left: 20px;
    color: var(--ink); font-weight: 700;
  }
  .contact-strip svg { flex: none; }
  .contact-email { top: 882px; font-size: 17px; }
  .contact-phone { top: 928px; height: 44px; font-size: 30px; }
  .contact-address { top: 980px; height: 48px; font-size: 15px; line-height: 1.05; }
</style>
</head>
<body>
  <main class="flyer">
    <div class="header-texture"></div>
    <div class="brand">
      <div class="brand-name">Ruv</div>
      <div class="brand-suffix">Pty Ltd</div>
    </div>
    <div class="photo photo-roadtrain" role="img" aria-label="Greyscale photo of a road train with side-tipper trailers on a dirt road"></div>

    <div class="photo photo-sunset-truck" role="img" aria-label="Colour photo of a white prime mover on an outback road at sunset"></div>

    <div class="services-band"></div>
    <h2 class="services-title">OUR SERVICES</h2>

    <ul class="service-list">
      <li>Over size loads / Hot Shot Load</li>
      <li>Heavy Vehicle Recovery Services</li>
      <li>Potable Water Deliveries</li>
      <li>Road Building / Maintenance</li>
      <li>Earthworks</li>
      <li>Sand &amp; Metal Supply &amp; Cartage</li>
      <li>Road Train Tippers</li>
      <li>Road Train Tankers</li>
      <li>Road Train Flat Tops</li>
      <li>Drop Deck Trailers</li>
      <li class="multi">Mine Site accredited equipment<br>&amp; Operators</li>
      <li>Traffic Management</li>
    </ul>

    <div class="quote-callout">
      <p class="quote-intro">We offer a large range services no listed so</p>
      <p class="quote-headline">Call us today for a<br>personalized quote<br>to suit your need.</p>
    </div>

    <div class="photo photo-oversize-truck" role="img" aria-label="Photo of a white truck hauling a grader on a low loader with an oversize sign"></div>

    <div class="contact-strip contact-email">
      <svg width="18" height="14" viewBox="0 0 18 14" aria-hidden="true"><rect x="1" y="1" width="16" height="12" fill="none" stroke="#111" stroke-width="2"/><path d="M1 1l8 7 8-7" fill="none" stroke="#111" stroke-width="2"/></svg>
      <span>info@ruvhaulage.com.au</span>
    </div>
    <div class="contact-strip contact-phone">
      <svg width="20" height="22" viewBox="0 0 24 24" aria-hidden="true"><path d="M6.6 10.8a15 15 0 006.6 6.6l2.2-2.2c.3-.3.7-.4 1-.2 1.1.4 2.3.6 3.6.6.6 0 1 .4 1 1V20c0 .6-.4 1-1 1C10.6 21 3 13.4 3 4c0-.6.4-1 1-1h3.5c.6 0 1 .4 1 1 0 1.3.2 2.5.6 3.6.1.3 0 .7-.2 1z" fill="#111"/></svg>
      <span>000 555 000</span>
    </div>
    <div class="contact-strip contact-address">
      <svg width="14" height="20" viewBox="0 0 14 20" aria-hidden="true"><path d="M7 0a7 7 0 00-7 7c0 5 7 13 7 13s7-8 7-13a7 7 0 00-7-7zm0 9.5A2.5 2.5 0 117 4.5a2.5 2.5 0 010 5z" fill="#111"/></svg>
      <span>Ruv Lot 114, Ridgeline Road<br>Dunmore Flat, Australia</span>
    </div>
  </main>
</body>
</html>
```